Lumen Path - Fiber Internet to the home postcard

Design a postcard for my company, Lumen Path, using the logo below. On the front of the card:
- No Buffering • No BS
- Second line should be the logo
- $60 / month • 10-Gigs
- lumenpath.net

Color palate should follow the colors in the logo.

Address should say
- Special pricing during construction
- Our best price
- Our fastest speed
- $60 / month • 10-Gigs
- lumenpath.net

Target Market(s)

25 - 55 year olds. Middle income/class. People with kids and pick up trucks

Industry/Entity Type

Fiber Internet Service Provider

Font styles to use
Sans Serif

Colors

Designer to choose colors to be used in the design.

Requirements
Nice to have
• I am open to more creative changes

```html
<!DOCTYPE html>
<html lang="en">
<head>
<meta charset="UTF-8">
<title>Lumen Path – Fiber Postcard</title>
<link href="https://fonts.googleapis.com/css2?family=Bebas+Neue&family=Barlow+Condensed:wght@300&display=swap" rel="stylesheet">
<style>
  :root {
    --page: #f7f7f7;
    --navy: #1f3566;
    --navy-deep: #1c2f5e;
    --teal: #2d5560;
    --green: #78c043;
    --forest: #1f4a2a;
    --ink: #1f2a6b;
    --white: #f5f5f5;
  }
  * { margin: 0; padding: 0; box-sizing: border-box; }
  html, body {
    width: 849px; height: 1200px; overflow: hidden;
    background: var(--page);
  }
  body { position: relative; font-family: "Bebas Neue", "Arial Narrow", sans-serif; color: var(--white); }

  .postcard {
    position: absolute; left: 62px; width: 730px; height: 519px;
    overflow: hidden;
    box-shadow: 0 2px 4px rgba(0,0,0,.35);
  }
  .postcard--front {
    top: 60px;
    background: linear-gradient(180deg, var(--navy) 0%, #2b4a5a 35%, #2f6a44 60%, var(--forest) 85%, #122a18 100%);
  }
  .postcard--back {
    top: 616px;
    background: linear-gradient(135deg, var(--green) 0%, #4f8a5c 35%, var(--teal) 65%, var(--navy-deep) 100%);
  }

  .family-photo {
    position: absolute; left: 361px; top: 139px; width: 369px; height: 380px;
    background:
      radial-gradient(ellipse at 60% 55%, rgba(214,170,120,.55) 0%, rgba(180,70,60,.35) 40%, rgba(40,70,90,0) 75%),
      linear-gradient(180deg, rgba(90,110,120,.2), rgba(60,80,110,.5));
  }
  .family-photo--faint {
    left: 380px; top: 220px; width: 350px; height: 299px;
    background: radial-gradient(ellipse at 60% 55%, rgba(120,140,170,.22) 0%, rgba(40,70,110,0) 70%);
  }

  .headline, .brand, .offer, .back-line {
    position: absolute; line-height: 1; white-space: nowrap; color: var(--white);
  }
  .headline { left: 32px; top: 152px; font-size: 69px; }
  .brand { left: 32px; top: 224px; font-size: 112px; letter-spacing: 1px; }
  .offer { left: 32px; top: 330px; font-size: 60px; }

  .url-box {
    position: absolute; background: var(--green);
    display: flex; align-items: center; justify-content: center;
    font-family: "Barlow Condensed", "Arial Narrow", sans-serif; font-weight: 300;
    color: var(--ink); font-size: 50px; line-height: 1;
  }
  .postcard--front .url-box { left: 0; top: 410px; width: 275px; height: 67px; }
  .postcard--back .url-box { left: 227px; top: 421px; width: 276px; height: 66px; }

  .back-line { left: 0; width: 730px; text-align: center; font-size: 58px; }
  .back-line--1 { top: 89px; }
  .back-line--2 { top: 139px; }
  .back-line--3 { top: 209px; }
  .back-line--4 { top: 267px; }
  .back-line--5 { top: 335px; }

  .divider { position: absolute; left: 132px; width: 465px; height: 2px; }
  .divider--top { top: 196px; }
  .divider--bottom { top: 322px; }
</style>
</head>
<body>

  <section class="postcard postcard--front">
    <div class="family-photo" role="img" aria-label="Photo of a smiling family looking at a tablet together, with glowing light rings"></div>
    <div class="headline">No Buffering•No BS</div>
    <div class="brand">Lumen Path</div>
    <div class="offer">$60/Month• 10-Gigs</div>
    <div class="url-box">lumenpath.net</div>
  </section>

  <section class="postcard postcard--back">
    <div class="family-photo family-photo--faint" role="img" aria-label="Faint background photo of a family using a tablet"></div>
    <div class="back-line back-line--1">Special Pricing During</div>
    <div class="back-line back-line--2">Construction</div>
    <svg class="divider divider--top" viewBox="0 0 465 2" preserveAspectRatio="none" aria-hidden="true">
      <line x1="0" y1="1" x2="465" y2="1" stroke="#f5f5f5" stroke-width="1" stroke-dasharray="6 7" opacity=".8"/>
    </svg>
    <div class="back-line back-line--3">Our Best Price</div>
    <div class="back-line back-line--4">Our Fastest Speed</div>
    <svg class="divider divider--bottom" viewBox="0 0 465 2" preserveAspectRatio="none" aria-hidden="true">
      <line x1="0" y1="1" x2="465" y2="1" stroke="#f5f5f5" stroke-width="1" stroke-dasharray="6 7" opacity=".8"/>
    </svg>
    <div class="back-line back-line--5">$60/Month• 10-Gigs</div>
    <div class="url-box">lumenpath.net</div>
  </section>

</body>
</html>
```